Copper Ridge Golf Circle Chart

I would like some type of design that can then be used on our website, like a png. or .jpeg or vector format. We want a circle/flow chart that describes our golf coaching process and has our logo faded in the background. attached is a rough draft to give you a general idea..something I created in word document but would like a much better version and attached is our logo. Our colors are red, black, and grey. The design does not necessarily have to have all of the bullet points..

Target Market(s)

Golfers, junior high golfers, high school golfers, adult golfers

Font styles to use
Sans Serif

Colors
ec1f27
f04a50
f59296
fbd4d5
aaaaaa
cbcbcb
1b1b1b
474747

Requirements
Nice to have
• Our colors are red, black, and grey, do not have to use all 3 in one design. Also The design does not necessarily have to have all of the bullet points.

```html
<!DOCTYPE html>
<html lang="en">
<head>
<meta charset="utf-8">
<title>Copper Ridge Golf – Coaching Process</title>
<link rel="stylesheet" href="https://fonts.googleapis.com/css2?family=Open+Sans:ital,wght@0,600;0,700;0,800;1,700&display=swap">
<style>
  :root {
    --red: #ec1f27;
    --charcoal: #474747;
    --ink: #1b1b1b;
    --mist: #cbcbcb;
    --faint: #e3e3e3;
    --white: #ffffff;
  }
  html, body {
    margin: 0;
    padding: 0;
    width: 1200px;
    height: 1000px;
    overflow: hidden;
    background: var(--white);
  }
  .process-graphic {
    display: block;
    width: 1200px;
    height: 1000px;
    font-family: "Open Sans", Arial, sans-serif;
  }
  .step-ring { fill: var(--white); stroke: var(--red); stroke-width: 7; }
  .step-label { fill: var(--charcoal); font-weight: 700; font-size: 18px; text-anchor: middle; }
  .flow-arrow { fill: none; stroke: var(--red); stroke-width: 12; stroke-linecap: round; }
  .flow-head { fill: var(--red); }
  .quadrant-dark { fill: var(--charcoal); }
  .quadrant-red { fill: var(--red); }
  .divider { stroke: var(--white); stroke-width: 6; }
  .quadrant-title { fill: var(--white); font-weight: 700; font-size: 28px; letter-spacing: 0.3px; }
  .title-rule { stroke: var(--white); stroke-width: 1; stroke-dasharray: 3 2; }
  .quadrant-point { fill: var(--white); font-weight: 700; font-style: italic; font-size: 15.5px; }
  .cycle-dark { fill: none; stroke: var(--charcoal); stroke-width: 17; }
  .cycle-red { fill: none; stroke: var(--red); stroke-width: 17; }
  .cycle-head-dark { fill: var(--charcoal); }
  .cycle-head-red { fill: var(--red); }
  .hub { fill: var(--white); }
  .hub-mark { fill: none; stroke: var(--faint); stroke-width: 3; }
  .brand-name { fill: var(--mist); font-weight: 700; font-size: 11px; text-anchor: middle; }
</style>
</head>
<body>
<svg class="process-graphic" viewBox="0 0 1200 1000" xmlns="http://www.w3.org/2000/svg" role="img" aria-label="Copper Ridge Golf coaching process: Evaluation, Coaching, Practice, Measure Progress">

  <!-- Compact cycle -->
  <g class="mini-cycle">
    <text class="brand-name" x="285" y="276">Copper Ridge</text>
    <text class="brand-name" x="285" y="291">Golf</text>

    <path class="flow-arrow" d="M350,125 Q360,185 385,205"/>
    <polygon class="flow-head" points="401,217 376,216 394,194"/>
    <path class="flow-arrow" d="M445,348 Q395,360 370,385"/>
    <polygon class="flow-head" points="356,399 380,395 360,375"/>
    <path class="flow-arrow" d="M222,440 Q205,380 185,365"/>
    <polygon class="flow-head" points="169,353 193,354 177,376"/>
    <path class="flow-arrow" d="M118,215 Q170,205 200,180"/>
    <polygon class="flow-head" points="215,167 209,191 191,169"/>

    <circle class="step-ring" cx="285" cy="107" r="62"/>
    <text class="step-label" x="285" y="113">Evaluation</text>
    <circle class="step-ring" cx="455" cy="280" r="62"/>
    <text class="step-label" x="455" y="286">Coaching</text>
    <circle class="step-ring" cx="285" cy="455" r="62"/>
    <text class="step-label" x="285" y="461">Practice</text>
    <circle class="step-ring" cx="113" cy="280" r="62"/>
    <text class="step-label" x="113" y="274">Measure</text>
    <text class="step-label" x="113" y="297">Progress</text>
  </g>

  <!-- Main quadrant chart -->
  <g class="quadrant-chart">
    <path class="quadrant-dark" d="M797,595 L437,595 A360,360 0 0 1 797,235 Z"/>
    <path class="quadrant-red" d="M797,595 L797,235 A360,360 0 0 1 1157,595 Z"/>
    <path class="quadrant-dark" d="M797,595 L1157,595 A360,360 0 0 1 797,955 Z"/>
    <path class="quadrant-red" d="M797,595 L797,955 A360,360 0 0 1 437,595 Z"/>
    <line class="divider" x1="797" y1="228" x2="797" y2="962"/>
    <line class="divider" x1="430" y1="595" x2="1164" y2="595"/>

    <g class="quadrant-copy evaluation">
      <text class="quadrant-title" x="557" y="378">EVALUATION</text>
      <line class="title-rule" x1="553" y1="389" x2="731" y2="389"/>
      <text class="quadrant-point" x="545" y="420">•  Video Swing Analysis</text>
      <text class="quadrant-point" x="545" y="463">•  Putting Report</text>
      <text class="quadrant-point" x="545" y="503">•  Develop A Plan</text>
    </g>

    <g class="quadrant-copy coaching">
      <text class="quadrant-title" x="853" y="378">COACHING</text>
      <line class="title-rule" x1="855" y1="389" x2="1006" y2="389"/>
      <text class="quadrant-point" x="855" y="420">•  Tour Quality Technology</text>
      <text class="quadrant-point" x="855" y="462">•  Visualization &amp; Feedback</text>
      <text class="quadrant-point" x="855" y="502">•  Understand Inconsistencies</text>
    </g>

    <g class="quadrant-copy measure-progress">
      <text class="quadrant-title" x="557" y="695">MEASURE</text>
      <text class="quadrant-title" x="557" y="730">PROGRESS</text>
      <line class="title-rule" x1="553" y1="741" x2="702" y2="741"/>
      <text class="quadrant-point" x="558" y="770">•  Track Progress</text>
      <text class="quadrant-point" x="572" y="797">With Data</text>
    </g>

    <g class="quadrant-copy practice">
      <text class="quadrant-title" x="843" y="730">PRACTICE</text>
      <line class="title-rule" x1="843" y1="741" x2="986" y2="741"/>
      <text class="quadrant-point" x="845" y="770">•  24 / 7 Access to Practice</text>
      <text class="quadrant-point" x="845" y="812">•  Practice With a Purpose</text>
    </g>

    <!-- Hub with cycle arrows -->
    <circle class="hub" cx="797" cy="595" r="102"/>
    <path class="cycle-dark" d="M800,510 A85,85 0 0 1 874,559"/>
    <polygon class="cycle-head-dark" points="883,579 890,551 858,567"/>
    <path class="cycle-red" d="M882,598 A85,85 0 0 1 833,672"/>
    <polygon class="cycle-head-red" points="813,681 841,688 825,656"/>
    <path class="cycle-dark" d="M794,680 A85,85 0 0 1 720,631"/>
    <polygon class="cycle-head-dark" points="711,611 704,639 736,623"/>
    <path class="cycle-red" d="M712,592 A85,85 0 0 1 761,518"/>
    <polygon class="cycle-head-red" points="781,509 753,502 769,534"/>

    <text class="brand-name" x="797" y="592">Copper Ridge</text>
    <text class="brand-name" x="797" y="607">Golf</text>
  </g>
</svg>
</body>
</html>
```